Commercial Business Card - stand out, clean, simple, unique.

commercial real estate group located in Texas. Called 4 Pines Real Estate. We want a unique yet clean and professional card. On one side I would like the 4P to be by itself or to look as unique or tasteful as possible. We have the logo in white, black, and color in case a black background or something similar looks best on one side. We need a space for our name, email, cell. website. And possibly room for a phrase or city.

Contact Information for Business Card

Name, Title, Email, Phone Number, website

```html
<!DOCTYPE html>
<html lang="en">
<head>
<meta charset="UTF-8">
<title>4 Pines Real Estate – Business Card</title>
<link rel="stylesheet" href="https://fonts.googleapis.com/css2?family=Cinzel:wght@400;600&family=Roboto:wght@400&display=swap">
<style>
  :root {
    --page-bg: #3a3a3c;
    --card-bg: #1f1f21;
    --card-edge: #151516;
    --mark-grey: #8c8c90;
    --text-white: #f2f2f2;
    --text-soft: #d6d6d6;
    --accent-orange: #e0672a;
    --band-blue-top: #2c4fa8;
    --band-blue-bottom: #1a1f3a;
  }
  * { margin: 0; padding: 0; box-sizing: border-box; }
  html, body {
    width: 799px;
    height: 1200px;
    overflow: hidden;
    background: var(--page-bg);
  }
  .canvas {
    position: relative;
    width: 799px;
    height: 1200px;
  }
  .card {
    position: absolute;
    left: 90px;
    width: 620px;
    height: 354px;
    border-radius: 26px;
    background: var(--card-bg);
    box-shadow: 0 2px 0 var(--card-edge), 0 18px 40px rgba(0,0,0,0.45);
    overflow: hidden;
  }
  .card-front { top: 120px; }
  .card-back { top: 720px; }

  /* Front */
  .front-mark {
    position: absolute;
    inset: 0;
    display: flex;
    align-items: center;
    justify-content: center;
    font-family: "Cinzel", serif;
    font-weight: 600;
    font-size: 170px;
    letter-spacing: -6px;
    color: var(--mark-grey);
  }

  /* Back */
  .side-band {
    position: absolute;
    left: 0; top: 0; bottom: 0;
    width: 62px;
    background: linear-gradient(180deg, var(--band-blue-top), var(--band-blue-bottom));
  }
  .side-rule {
    position: absolute;
    left: 66px; top: 0; bottom: 0;
    width: 3px;
    background: var(--accent-orange);
  }
  .brand-name {
    position: absolute;
    left: 100px;
    top: 38px;
    font-family: "Cinzel", serif;
    font-weight: 600;
    font-size: 34px;
    letter-spacing: 1px;
    color: var(--text-white);
  }
  .person {
    position: absolute;
    left: 100px;
    top: 120px;
  }
  .person-name {
    font-family: "Cinzel", serif;
    font-weight: 600;
    font-size: 24px;
    letter-spacing: 1px;
    color: var(--text-white);
  }
  .person-title {
    font-family: "Roboto", sans-serif;
    font-size: 15px;
    color: var(--text-soft);
    margin-top: 2px;
  }
  .contact-list {
    position: absolute;
    left: 100px;
    top: 200px;
    list-style: none;
    font-family: "Roboto", sans-serif;
    font-size: 16px;
    color: var(--text-white);
  }
  .contact-list li {
    display: flex;
    align-items: center;
    height: 26px;
  }
  .contact-icon {
    width: 14px;
    height: 14px;
    margin-right: 12px;
    flex: none;
  }
  .contact-list .no-icon { padding-left: 0; }
</style>
</head>
<body>
<main class="canvas">

  <section class="card card-front" aria-label="Card front">
    <div class="front-mark">4P</div>
  </section>

  <section class="card card-back" aria-label="Card back">
    <div class="side-band"></div>
    <div class="side-rule"></div>

    <div class="brand-name">4 Pines Real Estate</div>

    <div class="person">
      <div class="person-name">Marcus Reyes</div>
      <div class="person-title">Managing Director</div>
    </div>

    <ul class="contact-list">
      <li>
        <svg class="contact-icon" viewBox="0 0 16 16" aria-hidden="true">
          <path fill="#e0672a" d="M3 1.5l3 .5 1 3.5-2 1.3a9 9 0 0 0 4.2 4.2l1.3-2 3.5 1 .5 3-1.8 1.5C7.5 14 2 8.5 1.5 3.3z"/>
        </svg>
        512-555-0147
      </li>
      <li>
        <svg class="contact-icon" viewBox="0 0 16 16" aria-hidden="true">
          <rect x="1" y="3" width="14" height="10" rx="1" fill="#e0672a"/>
          <path d="M1.5 3.5L8 9l6.5-5.5" fill="none" stroke="#1f1f21" stroke-width="1.3"/>
        </svg>
        marcus@4pinesrealestate.com
      </li>
      <li>
        <svg class="contact-icon" viewBox="0 0 16 16" aria-hidden="true">
          <circle cx="8" cy="8" r="7" fill="#e0672a"/>
          <path d="M1 8h14M8 1c-3 3-3 11 0 14M8 1c3 3 3 11 0 14" fill="none" stroke="#1f1f21" stroke-width="1"/>
        </svg>
        www.4pinesrealestate.com
      </li>
      <li class="no-icon">410 Cedar Ridge Rd, Austin, TX 78701</li>
    </ul>
  </section>

</main>
</body>
</html>
```